Political Association Member Newsletter

We require a professional newsletter designed that will be sent both by mail and by email (and can be posted online) to the members in our client organization. I will develop and curate the content to send to the designer but we need help with a good design.

We have two key colours: red and blue (usually on white background). The pantones are:
blue = 301C
red = 032C

The logo I have from the client is attached as well as a recent piece with contact information and social media channels noted.

The client also provided a campaign logo "Build the Case for 2019" that will accompany copy for membership and donation which will follow.

Two preliminary content pieces are also included here: a flyer for a bbq and the "Regional Forum Digest" article.

Political

Sans Serif

• Space for pictures - uploaded below.

```html
<!DOCTYPE html>
<html lang="en">
<head>
<meta charset="utf-8">
<title>Regional Forum Digest</title>
<link href="https://fonts.googleapis.com/css2?family=Arimo:wght@400;700&family=Open+Sans:wght@600;700&display=swap" rel="stylesheet">
<style>
  :root {
    --red: #c8262c;
    --blue: #1a4f8c;
    --blue-deep: #123f73;
    --sky: #3ea0dc;
    --grey-band: #f1f1f1;
    --ink: #222;
    --muted: #666;
    --white: #fff;
  }
  * { margin: 0; padding: 0; box-sizing: border-box; }
  html, body { width: 1200px; height: 3422px; overflow: hidden; background: var(--white); }
  body { position: relative; font-family: "Arimo", Arial, sans-serif; color: var(--ink); }
  .abs { position: absolute; }

  .top-stripe { left: 0; top: 0; width: 1200px; height: 16px; background: var(--red); }
  .brand-mark { left: 59px; top: 50px; width: 80px; height: 80px; border-radius: 50%; background: var(--blue); }
  .brand-name { left: 158px; top: 62px; font-family: "Open Sans", sans-serif; font-weight: 700; font-size: 28px; line-height: 34px; color: var(--blue); }
  .issue-date { right: 59px; top: 90px; font-family: "Open Sans", sans-serif; font-weight: 700; font-size: 24px; color: var(--blue); }
  .rule-red { left: 0; top: 160px; width: 570px; height: 36px; background: var(--red); }
  .rule-blue { left: 611px; top: 160px; width: 589px; height: 36px; background: var(--blue); }
  .grey-band { left: 0; top: 196px; width: 1200px; height: 333px; background: var(--grey-band); }

  .photo { background: linear-gradient(160deg, #c9c4b8 0%, #8a7e6e 45%, #3c3a3c 100%); }
  .photo-hero { left: 59px; top: 217px; width: 1082px; height: 543px; }
  .photo-table { left: 59px; top: 1364px; width: 518px; height: 543px; background: linear-gradient(170deg, #2f4f86 0%, #4a3c3a 40%, #1c1c22 100%); }
  .photo-stage { left: 620px; top: 1364px; width: 521px; height: 347px; background: linear-gradient(180deg, #0d1b3a 0%, #2a4fa0 45%, #121a2c 100%); }

  .caption { font-family: "Open Sans", sans-serif; font-weight: 700; font-size: 20px; color: var(--muted); letter-spacing: 0.5px; }
  .caption-hero { left: 0; width: 1200px; top: 775px; text-align: center; }
  .caption-stage { left: 620px; top: 1740px; }
  .caption-table { left: 59px; top: 1932px; }

  .body-copy { left: 59px; width: 1082px; font-size: 35px; line-height: 47px; color: var(--ink); }
  .p1 { top: 830px; }
  .p2 { top: 1112px; }
  .p3 { top: 1986px; }
  .p4 { top: 2192px; }

  .btn { display: flex; align-items: center; justify-content: center; font-family: "Open Sans", sans-serif; font-weight: 700; color: var(--white); font-size: 24px; }
  .btn-more { left: 620px; top: 1836px; width: 215px; height: 71px; background: var(--blue); }
  .btn-contact { left: 988px; top: 2676px; width: 153px; height: 71px; background: var(--blue); font-size: 23px; }
  .btn-renew { left: 328px; top: 2813px; width: 539px; height: 68px; background: var(--red); font-size: 24px; }

  .signoff { right: 59px; top: 2498px; text-align: right; font-weight: 700; font-size: 34px; line-height: 52px; color: #333; }
  .signoff .email { color: var(--red); }

  .social { top: 2945px; display: flex; align-items: center; gap: 20px; font-family: "Open Sans", sans-serif; font-weight: 700; font-size: 29px; color: var(--blue); }
  .social .dot { width: 56px; height: 56px; border-radius: 50%; }
  .social-short { left: 59px; }
  .social-short .dot { background: var(--sky); }
  .social-short span { color: var(--sky); }
  .social-page { left: 532px; }
  .social-page .dot { background: var(--blue); }

  .footer { left: 0; top: 3062px; width: 1200px; height: 328px; background: var(--blue); }
  .footer-col { top: 3118px; font-size: 28px; line-height: 55px; color: var(--white); }
  .footer-left { left: 59px; }
  .footer-right { right: 59px; text-align: right; }
  .legal-bar { left: 0; top: 3390px; width: 1200px; height: 32px; background: var(--blue-deep); }
  .legal { top: 3393px; font-size: 22px; color: #dfe6f0; }
  .legal-left { left: 59px; }
  .legal-right { right: 59px; }
  .legal-right .unsub { color: var(--red); }
</style>
</head>
<body>
  <div class="abs top-stripe"></div>
  <div class="abs brand-mark"></div>
  <div class="abs brand-name">Prairie Civic Association,<br>River Centre</div>
  <div class="abs issue-date">Sturday August 13,2016</div>
  <div class="abs rule-red"></div>
  <div class="abs rule-blue"></div>
  <div class="abs grey-band"></div>

  <div class="abs photo photo-hero" role="img" aria-label="Three smiling men standing arm in arm at the national convention hall"></div>
  <div class="abs caption caption-hero">PHOTO DESCR.</div>

  <p class="abs body-copy p1">It’s my pleasure to introduce myself as the newest member of National Council from Alberta. I will join Joan Bellamy from Calgary representing the views of members from across the province. I’ve met many of you over the years, in particular during my three years as EDA President in River Centre, and I’m looking forward to working for you again.</p>
  <p class="abs body-copy p2">The 2016 Civic Association National Convention was a remarkable success. Our Party took important steps toward building a foundation for a broader coalition of members, we said thank you to former Prime Minister Arthur Penrose, and we heard compelling narratives for what lies ahead.</p>

  <div class="abs photo photo-table" role="img" aria-label="Delegates seated along a long table at the convention, stage screens behind"></div>
  <div class="abs photo photo-stage" role="img" aria-label="Wide view of the convention stage under blue lights with a large audience"></div>
  <div class="abs caption caption-stage">PHOTO DESCR.</div>
  <div class="abs btn btn-more">SEE MORE</div>
  <div class="abs caption caption-table">PHOTO DESCR.</div>

  <p class="abs body-copy p3">We also elected Neil Carver as our new Party President. Neil is a Vancouver-based lawyer with a keen sense of the issues that need to be addressed in the months ahead. I trust you’ll join me in congratulating Neil!</p>
  <p class="abs body-copy p4">I know many of you have a busy summer ahead, but I encourage you to stay engaged with your EDA and our Party. Join us at the Northern Region Civic BBQ on August 13, volunteer for a leadership campaign, or encourage your neighbours to become members and join our team. Together we can put out Party in a position to bring better government back to our great country!</p>

  <div class="abs signoff">Daniel Marsh<br>National Council<br><span class="email">daniel.marsh@rivercentre-civic.org</span></div>
  <div class="abs btn btn-contact">CONTACT ME</div>
  <div class="abs btn btn-renew">RENEW YOUR MEMBERSHIP TODAY!</div>

  <div class="abs social social-short"><div class="dot"></div><span>@RiverCentreCA</span></div>
  <div class="abs social social-page"><div class="dot"></div><span>River Centre Civic Association</span></div>

  <div class="abs footer"></div>
  <div class="abs footer-col footer-left">Northern Region Area Office<br>Summer BBQ<br>#210, 4480 Lakeview Road NW<br>Edmonton, AB T5X 0A0</div>
  <div class="abs footer-col footer-right">Phone: 0012 555 01 20<br>0012 555 01 21<br>Fax : 0023 555 01 22<br>E-mail : info@rivercentre-civic.org</div>
  <div class="abs legal-bar"></div>
  <div class="abs legal legal-left">This is E-mail 2016. All Rights Reserved.</div>
  <div class="abs legal legal-right">View This E-mail Online &nbsp;|&nbsp; <span class="unsub">Unsubscribe</span></div>
</body>
</html>
```